high end contractor

high end contracting company we do all phases of construction kitchen,bathrooms,etc... please look at my website before you design www.harborkeybuild.com

would love some sort of lines or logo or both

Industry/Entity Type

Construction

Contact Information for Business Card

company name: oak & meridian contracting address: 318 fenwick st Lakeport NY 10690 email: harborkeybuild@mailbrook.com website: www.harborkeybuild.com office#: 914-208-3916 fax#: 914-208-5523 dominic valtersen mobile# 917-526-0389

```html
<!DOCTYPE html>
<html lang="en">
<head>
<meta charset="utf-8">
<title>Oak &amp; Meridian Renovations — Business Card</title>
<link href="https://fonts.googleapis.com/css2?family=Open+Sans:wght@300;400;600&display=swap" rel="stylesheet">
<style>
  :root {
    --backdrop: #a8fbf9;
    --teal: #45c1c0;
    --teal-bright: #4fd6d4;
    --charcoal: #2b2b2d;
    --panel: rgba(40, 40, 42, 0.86);
    --white: #ffffff;
  }
  * { margin: 0; padding: 0; box-sizing: border-box; }
  html, body {
    width: 1200px; height: 900px; overflow: hidden;
    background: var(--backdrop);
    font-family: "Open Sans", Arial, sans-serif;
  }
  .sheet {
    width: 1200px; height: 900px;
    display: flex; flex-direction: column; align-items: center; justify-content: center;
    gap: 40px;
  }
  .card {
    position: relative; width: 680px; height: 389px; overflow: hidden;
    box-shadow: 0 6px 18px rgba(0,0,0,0.18);
  }

  /* Front */
  .front-photo {
    position: absolute; inset: 0;
    background:
      linear-gradient(160deg, transparent 55%, rgba(74,52,38,0.85) 80%, #3d2a1e 100%),
      linear-gradient(100deg, #8d8f92 0%, #d9dadb 22%, #f1f1f0 45%, #bfc1c3 62%, #e8e8e6 80%, #9a9c9e 100%);
  }
  .title-band {
    position: absolute; top: 22px; left: 0; width: 520px; height: 54px;
    background: var(--panel);
    border-bottom: 2px solid var(--teal);
    display: flex; align-items: center; padding-left: 18px;
    font-size: 30px; letter-spacing: 0.5px; text-transform: uppercase; white-space: nowrap;
  }
  .title-band .firm { color: var(--teal-bright); font-weight: 400; }
  .title-band .trade { color: var(--white); font-weight: 400; margin-left: 10px; }

  .contact-panel {
    position: absolute; top: 128px; left: 0; width: 360px; height: 176px;
    background: var(--panel);
    padding: 14px 18px;
  }
  .contact-name {
    color: var(--teal-bright); font-size: 23px; font-weight: 400;
    text-transform: uppercase; letter-spacing: 0.5px; margin-bottom: 8px;
  }
  .contact-list { list-style: none; }
  .contact-list li {
    display: flex; align-items: center; gap: 10px;
    color: var(--white); font-size: 17px; line-height: 28px;
  }
  .contact-list svg { width: 18px; height: 18px; flex: none; }

  .address-strip {
    position: absolute; bottom: 22px; left: 0; width: 470px; height: 42px;
    background: var(--panel);
    border-top: 2px solid var(--teal);
    display: flex; align-items: center; gap: 10px; padding-left: 16px;
    color: var(--white); font-size: 19px; white-space: nowrap;
  }
  .address-strip svg { width: 18px; height: 22px; flex: none; }

  /* Back */
  .back svg { display: block; }
  .back-name { font-family: "Open Sans", Arial, sans-serif; font-size: 26px; font-weight: 600; fill: var(--charcoal); }
  .back-web { font-family: "Open Sans", Arial, sans-serif; font-size: 22px; font-weight: 400; fill: var(--charcoal); }
</style>
</head>
<body>
<main class="sheet">

  <section class="card front">
    <div class="front-photo" role="img" aria-label="Photo of a bright renovated kitchen with white cabinets, stainless refrigerator and dark wood floor"></div>

    <div class="title-band">
      <span class="firm">Oak &amp; Meridian</span><span class="trade">Renovations</span>
    </div>

    <div class="contact-panel">
      <p class="contact-name">Dominic Valtersen</p>
      <ul class="contact-list">
        <li>
          <svg viewBox="0 0 18 18" fill="none" stroke="var(--teal-bright)" stroke-width="1.6"><rect x="5" y="1.5" width="8" height="15" rx="1.5"/><line x1="8" y1="14" x2="10" y2="14"/></svg>
          917-526-0389
        </li>
        <li>
          <svg viewBox="0 0 18 18" fill="var(--teal-bright)"><path d="M4 2l3 3-1.6 2.2c1 2 2.4 3.4 4.4 4.4L12 10l3 3-2 2.5C7.5 15 3 10.5 2.5 4z"/></svg>
          914-208-3916
        </li>
        <li>
          <svg viewBox="0 0 18 18" fill="var(--teal-bright)"><rect x="5" y="2" width="8" height="5"/><rect x="2" y="7" width="14" height="7" rx="1"/><rect x="5" y="12" width="8" height="4" fill="var(--white)"/></svg>
          914-208-5523
        </li>
        <li>
          <svg viewBox="0 0 18 18" fill="none" stroke="var(--teal-bright)" stroke-width="1.6"><rect x="1.5" y="4" width="15" height="10"/><polyline points="1.5,4 9,10 16.5,4"/></svg>
          harborkeybuild@mailbrook.com
        </li>
      </ul>
    </div>

    <div class="address-strip">
      <svg viewBox="0 0 18 22" fill="var(--teal-bright)"><path d="M9 1a7 7 0 0 0-7 7c0 5 7 13 7 13s7-8 7-13a7 7 0 0 0-7-7zm0 10a3 3 0 1 1 0-6 3 3 0 0 1 0 6z"/></svg>
      318 Fenwick St. Lakeport NY 10690
    </div>
  </section>

  <section class="card back">
    <svg width="680" height="389" viewBox="0 0 680 389">
      <defs>
        <linearGradient id="band-kitchen" x1="0" y1="0" x2="1" y2="1">
          <stop offset="0" stop-color="#d6d8d9"/><stop offset="0.5" stop-color="#8a7b6c"/><stop offset="1" stop-color="#e9e9e7"/>
        </linearGradient>
        <linearGradient id="band-wood" x1="0" y1="0" x2="1" y2="0">
          <stop offset="0" stop-color="#7a5038"/><stop offset="0.4" stop-color="#c98a62"/><stop offset="1" stop-color="#8c5a3c"/>
        </linearGradient>
        <linearGradient id="band-bath" x1="0" y1="0" x2="1" y2="0">
          <stop offset="0" stop-color="#b9b6b0"/><stop offset="0.6" stop-color="#f1efe6"/><stop offset="1" stop-color="#8f8d88"/>
        </linearGradient>
        <linearGradient id="band-marble" x1="0" y1="0" x2="1" y2="0">
          <stop offset="0" stop-color="#8a6a52"/><stop offset="0.5" stop-color="#cbbfb2"/><stop offset="1" stop-color="#a79c91"/>
        </linearGradient>
      </defs>

      <polygon class="teal-field" points="0,0 680,0 680,250 0,30" fill="var(--teal)"/>

      <polygon points="0,30 680,250 680,330 0,110" fill="url(#band-kitchen)" role="img" aria-label="Photo strip of a modern kitchen with shelving"/>
      <polygon points="0,110 680,330 680,389 0,195" fill="url(#band-wood)" role="img" aria-label="Photo strip of a wooden vanity and wood panelling"/>
      <polygon points="0,195 680,389 560,389 0,275" fill="url(#band-bath)" role="img" aria-label="Photo strip of a bathroom with a lit oval mirror"/>
      <polygon points="0,275 560,389 0,389" fill="url(#band-marble)" role="img" aria-label="Photo strip of a marble-tiled bathroom floor"/>

      <g stroke="var(--teal-bright)" stroke-width="3">
        <line x1="0" y1="30" x2="680" y2="250"/>
        <line x1="0" y1="110" x2="680" y2="330"/>
        <line x1="0" y1="195" x2="680" y2="389"/>
        <line x1="0" y1="275" x2="560" y2="389"/>
      </g>

      <circle cx="262" cy="72" r="12" fill="var(--charcoal)"/>
      <text class="back-name" x="284" y="81">Oak &amp; Meridian</text>
      <text class="back-web" x="650" y="44" text-anchor="end">www.harborkeybuild.com</text>
    </svg>
  </section>

</main>
</body>
</html>
```